BrightLane Driving School

I need a Facebook page for my Driving School. I teach mostly teenagers how to drive in New Hampshire but also do private classes for adults as well. More info can be found at brightlanelessons.com

```html
<!DOCTYPE html>
<html lang="en">
<head>
<meta charset="utf-8">
<title>BrightLane Driving School</title>
<link href="https://fonts.googleapis.com/css2?family=Barlow:wght@600;800&family=Russo+One&display=swap" rel="stylesheet">
<style>
  :root {
    --ink: #0d0d0d;
    --amber: #f4b733;
    --white: #ffffff;
    --yellow-hi: #f6dc10;
    --yellow: #eec21a;
    --orange: #d99522;
    --bronze: #8a5a14;
    --shadow: #3a2606;
  }
  * { margin: 0; padding: 0; box-sizing: border-box; }
  html, body { width: 1200px; height: 457px; overflow: hidden; background: var(--white); }
  .cover {
    position: relative;
    width: 1200px;
    height: 457px;
    overflow: hidden;
    font-family: "Barlow", Arial, sans-serif;
  }
  .tunnel-photo {
    position: absolute;
    inset: 0;
    background:
      radial-gradient(ellipse 260px 90px at 560px 150px, rgba(255,250,210,0.85), rgba(255,250,210,0) 70%),
      radial-gradient(ellipse 420px 260px at 1020px 330px, rgba(70,45,10,0.55), rgba(70,45,10,0) 75%),
      linear-gradient(100deg, var(--yellow-hi) 0%, var(--yellow) 30%, var(--orange) 58%, var(--bronze) 85%, var(--shadow) 100%);
  }
  .brand {
    position: absolute;
    left: 28px;
    top: 28px;
    display: flex;
    align-items: center;
    gap: 58px;
  }
  .brand-dot {
    width: 130px;
    height: 130px;
    border-radius: 50%;
    background: var(--ink);
  }
  .brand-name {
    font-weight: 800;
    font-size: 78px;
    line-height: 1;
    color: var(--ink);
    letter-spacing: 1px;
    margin-top: -60px;
  }
  .service {
    position: absolute;
    width: 503px;
    height: 58px;
    background: var(--ink);
    color: var(--amber);
    font-weight: 600;
    font-size: 26px;
    letter-spacing: 0.6px;
    display: flex;
    align-items: center;
  }
  .service--teen { left: 252px; top: 121px; padding-left: 11px; }
  .service--individual { left: 342px; top: 202px; padding-left: 34px; }
  .service--senior { left: 447px; top: 280px; padding-left: 51px; }
  .phone {
    position: absolute;
    left: 650px;
    top: 360px;
    font-family: "Russo One", Arial, sans-serif;
    font-style: italic;
    font-size: 58px;
    line-height: 1;
    color: var(--white);
    letter-spacing: 1px;
    transform: skewX(-8deg);
  }
</style>
</head>
<body>
  <main class="cover">
    <div class="tunnel-photo" role="img" aria-label="Motion-blurred view from inside a car speeding through a lit tunnel, dashboard and side mirror in golden light"></div>

    <div class="brand">
      <span class="brand-dot"></span>
      <span class="brand-name">BrightLane</span>
    </div>

    <div class="service service--teen">TEENAGE GROUP DRIVER EDUCATION</div>
    <div class="service service--individual">INDIVIDUAL DRIVER EDUCATION</div>
    <div class="service service--senior">SENIOR DRIVER EVALUATIONS</div>

    <div class="phone">603-555-0148</div>
  </main>
</body>
</html>
```